Brellwick Motor Finance- Free Oil Change letters

this is A Letter from my Used Car Sales & Service business. Specifically this is in a large window envelope (See Web Links) A free oil change to get this specific customer to open the envelope. The free oil change is the top have of the letter stuff in 4 1/8 x 9 open window envelope. The rest of letter is to the Fresh bankruptcy people. The coupon is to get them to open and read my offer. I had the combined ideas from the moving target link attached.
the middle of the envelope has to have a customer name address for postal delivery
I have also included our company website and our logo to be contained. This has to be in a letter program that I will mail merge a database mailer to print.

This project is for only what will be view through the large window envelope

my company website
http://www.tovbmf.com/

envelope I use
http://www.mailwrapdepot.net/wrappers/pane/clear-pane/wrapper-71936.html

Envelope Dimensions: 4 1/8 x 9 1/2
Window Dimensions: 3 x 8 (From Left Edge: 3/4 - From Bottom Edge: 1/2)

the whole point is the make this look highend to get the customer to want read the letter.. The Letter will talk about We are the Second Change Credit Expert and to come to us to buy a used car.

```html
<!DOCTYPE html>
<html lang="en">
<head>
<meta charset="utf-8">
<title>Brellwick Motor Finance – Free Oil Change Window Insert</title>
<link href="https://fonts.googleapis.com/css2?family=Bebas+Neue&family=Open+Sans:wght@400;700&display=swap" rel="stylesheet">
<style>
  :root {
    --page-bg: #2e2e2e;
    --panel-black: #0b0909;
    --photo-dark: #151313;
    --photo-mid: #2f2c2b;
    --photo-light: #55504c;
    --lime: #b8cd2b;
    --gold: #f3c813;
    --white: #ffffff;
  }
  * { margin: 0; padding: 0; box-sizing: border-box; }
  html, body {
    width: 1200px;
    height: 800px;
    overflow: hidden;
    background: var(--page-bg);
  }
  .window-insert {
    position: absolute;
    left: 48px;
    top: 193px;
    width: 1104px;
    height: 414px;
    border-radius: 5px;
    overflow: hidden;
    background: var(--panel-black);
  }
  .oil-photo {
    position: absolute;
    left: 484px;
    top: 0;
    width: 620px;
    height: 100%;
    background:
      radial-gradient(ellipse 55% 70% at 80% 20%, var(--photo-light) 0%, var(--photo-mid) 45%, transparent 80%),
      linear-gradient(90deg, var(--photo-dark) 0%, var(--photo-mid) 60%, #3a3634 100%);
  }
  .mailing-block {
    position: absolute;
    left: 36px;
    top: 40px;
    font-family: "Open Sans", Arial, sans-serif;
    font-weight: 700;
    font-size: 15.5px;
    line-height: 21px;
    color: var(--white);
  }
  .offer-headline {
    position: absolute;
    left: 34px;
    top: 140px;
    font-family: "Bebas Neue", Impact, sans-serif;
    font-size: 132px;
    line-height: 1;
    letter-spacing: 1px;
    white-space: nowrap;
    color: var(--gold);
  }
  .offer-headline .free { color: var(--lime); }
  .website {
    position: absolute;
    left: 36px;
    top: 328px;
    font-family: "Open Sans", Arial, sans-serif;
    font-size: 29px;
    color: var(--white);
  }
  .brand-name {
    position: absolute;
    right: 32px;
    top: 306px;
    width: 200px;
    text-align: right;
    font-family: "Open Sans", Arial, sans-serif;
    font-weight: 700;
    font-size: 24px;
    line-height: 29px;
    color: var(--gold);
  }
</style>
</head>
<body>
  <main class="window-insert">
    <div class="oil-photo" role="img" aria-label="Photo of golden motor oil pouring from a bottle into an engine filler neck"></div>

    <div class="mailing-block">
      <p>Address: XXX XXX XXX</p>
      <p>Street: XXX XXX XXX 99</p>
      <p>Name: XXXXXX XXXXXXXX</p>
    </div>

    <h1 class="offer-headline"><span class="free">FREE</span> OIL CHANGE</h1>

    <p class="website">www.tovbmf.com</p>

    <p class="brand-name">Brellwick Motor Finance</p>
  </main>
</body>
</html>
```